Kestrel Orchard Fliers and logo design

We need to design a product logo and some informational fliers for a pebble quest.
I have attached our Kestrel Orchard logo - colours need to be complimentary but not the same, we would like fresh, funky but still professional. We generally communicate in a fairly casual way to reach our market. (We don't like boring)
Clear and simple - not too busy
images are good but not actual photos
Here is our website to give you an idea www.kestrelorchard.co.nz
The flier is a 3 page document.
The logo is to say Pebble Quest. The challenge is based on exercise, connecting with people, giving, learning and taking notice (The 7 stones of Marlow) Once agin the logo needs to be complementary but not the same.
The Kestrel orchard logo needs to be on the fliers but the pebble quest logo is separate.
Thanks very much!!

```html
<!DOCTYPE html>
<html lang="en">
<head>
<meta charset="utf-8">
<title>Kestrel Orchard – Pebble Quest Fliers</title>
<link rel="stylesheet" href="https://fonts.googleapis.com/css2?family=Lato:wght@400;700;900&family=Roboto+Slab:wght@700&display=swap">
<style>
  :root {
    --backdrop: #9b9b9b;
    --paper: #ffffff;
    --teal: #4cc0a0;
    --teal-dark: #35a886;
    --lime: #9fcf2c;
    --lime-dark: #6aa51c;
    --panel: #ececec;
    --ink: #333333;
    --ink-soft: #555555;
    --berry: #b5213a;
    --line: #b9b9b9;
  }
  * { box-sizing: border-box; margin: 0; padding: 0; }
  html, body { width: 1200px; height: 638px; overflow: hidden; }
  body {
    background: var(--backdrop);
    font-family: "Lato", Arial, sans-serif;
    color: var(--ink);
    position: relative;
  }
  .page {
    position: absolute;
    top: 100px;
    width: 309px;
    height: 434px;
    background: var(--paper);
    overflow: hidden;
  }
  .page--stress { left: 48px; }
  .page--values { left: 446px; }
  .page--tips { left: 846px; }

  .site-bar {
    position: absolute; left: 0; right: 0; bottom: 0; height: 6px;
    background: var(--berry);
  }
  .site-url {
    position: absolute; left: 0; right: 0; bottom: 12px;
    text-align: center; font-size: 5.6px; letter-spacing: 1.4px; color: var(--ink);
  }
  .brand {
    position: absolute; display: flex; align-items: center; gap: 4px;
    font-weight: 700; color: var(--teal-dark);
  }
  .brand__dot { width: 12px; height: 12px; border-radius: 50%; background: var(--teal); }

  /* Page 1 */
  .stress__hero {
    position: absolute; left: 0; top: 0; width: 309px; height: 196px;
  }
  .stress__brand { left: 14px; top: 12px; font-size: 12px; }
  .stress__banner {
    position: absolute; left: 0; top: 196px; width: 100%; height: 32px;
    background: var(--teal);
    font-family: "Roboto Slab", Georgia, serif; font-weight: 700;
    color: #fff; font-size: 23px; text-align: center; line-height: 32px; letter-spacing: 0.3px;
  }
  .stress__intro {
    position: absolute; left: 12px; top: 234px; width: 140px;
  }
  .stress__lead {
    color: var(--teal-dark); font-weight: 700; font-size: 9px; line-height: 1.15; margin-bottom: 5px;
  }
  .body-copy { font-size: 4.5px; line-height: 1.4; color: var(--ink-soft); text-align: justify; }
  .body-copy p { margin-bottom: 4px; }
  .stress__steps {
    position: absolute; left: 152px; top: 228px; width: 157px; height: 182px;
    background: var(--panel); padding: 6px 8px;
  }
  .step__title { color: var(--teal-dark); font-weight: 700; font-size: 8px; line-height: 1.1; }
  .step__title--sub { font-size: 7px; margin-left: 6px; }
  .step__text { font-size: 4.5px; line-height: 1.35; color: var(--ink-soft); margin-bottom: 4px; }
  .step__text--sub { margin-left: 6px; }

  /* Page 2 */
  .values__hero { position: absolute; left: 0; top: 0; width: 309px; height: 120px; }
  .values__brand { right: 10px; top: 118px; font-size: 7px; }
  .values__title {
    position: absolute; left: 12px; top: 136px;
    color: var(--teal); font-weight: 700; font-size: 19px;
  }
  .values__lead {
    position: absolute; left: 12px; top: 158px; width: 290px;
    font-weight: 700; font-size: 5.3px; color: var(--ink);
  }
  .values__step {
    position: absolute; left: 12px; top: 166px;
    color: var(--teal); font-weight: 700; font-size: 10px;
  }
  .values__hint {
    position: absolute; left: 12px; top: 181px; width: 285px;
    font-weight: 700; font-size: 4.3px; line-height: 1.35; color: var(--ink);
  }
  .values__list {
    position: absolute; top: 197px; width: 96px; list-style: none;
    font-size: 4.4px; color: var(--ink-soft);
  }
  .values__list li { height: 7.6px; line-height: 7.6px; padding-left: 6px; position: relative; white-space: nowrap; }
  .values__list li.wrap { height: 12px; line-height: 1.35; white-space: normal; padding-top: 1px; }
  .values__list li::before {
    content: ""; position: absolute; left: 0; top: 3px; width: 2px; height: 2px;
    border-radius: 50%; background: var(--teal);
  }
  .values__list--a { left: 12px; }
  .values__list--b { left: 108px; }
  .values__list--c { left: 204px; }

  /* Page 3 */
  .tips__upper { position: absolute; left: 12px; top: 9px; width: 287px; }
  .tips__heading { color: var(--teal); font-weight: 700; font-size: 10px; line-height: 1.1; }
  .tips__text { font-size: 4.5px; line-height: 1.35; color: var(--ink); margin-bottom: 4px; }
  .tips__blanks { list-style: none; font-size: 4.8px; font-weight: 700; margin-bottom: 4px; }
  .tips__blanks li { display: flex; align-items: flex-end; height: 10.5px; }
  .tips__blanks li span { flex: 1; border-bottom: 0.7px solid var(--line); margin-left: 6px; height: 6px; }
  .tips__panel {
    position: absolute; left: 0; top: 116px; width: 309px; height: 292px;
    background: var(--panel); padding: 7px 12px;
  }
  .tips__panel .tips__heading { font-size: 10px; margin-bottom: 3px; }
  .tips__intro { font-size: 4.4px; font-weight: 700; line-height: 1.4; margin-bottom: 5px; }
  .tip { font-size: 4.3px; line-height: 1.4; color: var(--ink-soft); margin-bottom: 4.5px; }
  .tip__name { color: var(--teal-dark); font-weight: 700; font-size: 5.4px; }
  .tips__brand { left: 50%; transform: translateX(-50%); top: 386px; font-size: 7px; }
</style>
</head>
<body>

<!-- Stress Buster page -->
<section class="page page--stress">
  <svg class="stress__hero" viewBox="0 0 309 196" role="img" aria-label="Photo of smiling fingertips with drawn happy faces on a bright green background">
    <defs>
      <radialGradient id="limeGlow" cx="0.6" cy="0.35" r="0.8">
        <stop offset="0" stop-color="#c9e84a"/>
        <stop offset="1" stop-color="#6aa51c"/>
      </radialGradient>
      <linearGradient id="skin" x1="0" y1="0" x2="0" y2="1">
        <stop offset="0" stop-color="#e9c5a5" stop-opacity="0"/>
        <stop offset="0.4" stop-color="#e0b590" stop-opacity="0.85"/>
        <stop offset="1" stop-color="#d7a57f"/>
      </linearGradient>
    </defs>
    <rect width="309" height="196" fill="url(#limeGlow)"/>
    <rect y="80" width="309" height="116" fill="url(#skin)"/>
    <polygon points="0,0 309,0 309,20 0,66" fill="#fff"/>
  </svg>
  <div class="brand stress__brand"><span class="brand__dot"></span>Kestrel Orchard</div>
  <div class="stress__banner">STRESS BUSTER!</div>

  <div class="stress__intro">
    <p class="stress__lead">We cannot control what happens to us in life, but we can change the way we react</p>
    <div class="body-copy">
      <p>Stress happens because we are allowing fear, anger, disappointment and a host of other negative emotions to navigate our actions. By becoming aware of these emotions and allowing them to simply be, we can begin to gain control of how we react and respond to stressful situations.</p>
      <p>Our experience is always changing. Without awareness, mental patterns related to what we fear and what upsets us make life harder.</p>
      <p>S.T.O.P is a powerful, yet surprisingly basic strategy that helps you to be focused, alert, relaxed and at your emotional best when stressful moments present themselves in your life.</p>
      <p>Simply put, it's a four-step checklist to use anytime you want to ground yourself and get some insight into whatever is going on. The whole idea behind it is that by taking a very brief break—even less than one minute—you can determine the very best action to take in the moment.</p>
    </div>
  </div>

  <div class="stress__steps">
    <p class="step__title">S = Stop</p>
    <p class="step__text">Stop what you are doing: Press the pause button on your thoughts and actions.</p>
    <p class="step__title">T = Take</p>
    <p class="step__text">Take a few deep breaths to centre yourself and bring yourself fully into the present moment.</p>
    <p class="step__title">O = Observe</p>
    <p class="step__text">Observe what is going on with your:</p>
    <p class="step__title step__title--sub">1. Body</p>
    <p class="step__text step__text--sub">What physical sensations are you aware of (touch, sight, hearing, taste, smell)?</p>
    <p class="step__title step__title--sub">Emotions</p>
    <p class="step__text step__text--sub">What are you feeling right now?</p>
    <p class="step__title step__title--sub">2. Mind</p>
    <p class="step__text step__text--sub">What assumptions are you making about your feelings? What is the story you're telling yourself about why you are having them?</p>
    <p class="step__title">P = Proceed</p>
    <p class="step__text">Proceed with whatever you were doing, making a conscious, intentional choice to incorporate what you just learned.</p>
  </div>

  <p class="site-url">www.kestrelorchard.co.nz</p>
  <div class="site-bar"></div>
</section>

<!-- Values page -->
<section class="page page--values">
  <svg class="values__hero" viewBox="0 0 309 120" role="img" aria-label="Photo of three cheering office workers celebrating at a desk by a city window">
    <defs>
      <linearGradient id="officeLight" x1="0" y1="0" x2="1" y2="1">
        <stop offset="0" stop-color="#cfdbe6"/>
        <stop offset="0.55" stop-color="#9fb5c8"/>
        <stop offset="1" stop-color="#4d6478"/>
      </linearGradient>
    </defs>
    <rect width="309" height="120" fill="url(#officeLight)"/>
    <polygon points="0,116 309,100 309,104 0,120" fill="#4cc0a0"/>
    <polygon points="0,120 309,104 309,120" fill="#fff"/>
  </svg>
  <div class="brand values__brand"><span class="brand__dot"></span>Kestrel Orchard</div>

  <h1 class="values__title">Values</h1>
  <p class="values__lead">This exercise is designed to help you reach a better understanding of your most significant values.</p>
  <h2 class="values__step">Step 1: What I Value Most...</h2>
  <p class="values__hint">From this list of values (both work and personal), select the ten that are most important to you - as guides for how to behave, or as components of a valued way of life. Feel free to add any values of your own to this list.</p>

  <ul class="values__list values__list--a">
    <li>Achievement</li><li>Advancement and promotion</li><li>Adventure</li><li>Affection (love and caring)</li><li>Arts</li><li>Challenging problems</li><li>Change and variety</li><li>Close relationships</li><li>Community</li><li>Competence</li><li>Competition</li><li>Cooperation</li><li>Country</li><li>Creativity</li><li>Decisiveness</li><li>Democracy</li><li>Ecological awareness</li><li>Economic security</li><li>Effectiveness</li><li>Efficiency</li><li>Ethical practice</li><li>Excellence</li><li>Excitement</li><li>Fame</li><li>Fast living</li><li>Financial gain</li><li>Freedom</li>
  </ul>
  <ul class="values__list values__list--b">
    <li>Friendships</li><li>Growth</li><li>Having a family</li><li>Helping other people</li><li>Helping society</li><li>Honesty</li><li>Independence</li><li>Influencing others</li><li>Inner harmony</li><li>Integrity</li><li>Intellectual status</li><li>Involvement</li><li>Job tranquility</li><li>Knowledge</li><li>Leadership</li><li>Location</li><li>Loyalty</li><li>Market position</li><li>Meaningful work</li><li>Merit</li><li>Money</li><li>Nature</li><li class="wrap">Being around people who are open and honest</li><li>Order (tranquility, stability, conformity)</li><li>Personal development</li>
  </ul>
  <ul class="values__list values__list--c">
    <li>Physical challenge</li><li>Pleasure</li><li>Power and authority</li><li>Privacy</li><li>Public service</li><li>Purity</li><li>Quality of what I take part in</li><li>Quality relationships</li><li class="wrap">Recognition (respect from others, status)</li><li>Religion</li><li>Reputation</li><li>Responsibility and accountability</li><li>Security</li><li>Self-Respect</li><li>Serenity</li><li>Sophistication</li><li>Stability</li><li>Status</li><li>Supervising others</li><li>Time freedom</li><li>Truth</li><li>Wealth</li><li>Wisdom</li><li>Work under pressure</li><li>Work with others</li><li>Working alone</li>
  </ul>

  <p class="site-url">www.kestrelorchard.co.nz</p>
  <div class="site-bar"></div>
</section>

<!-- Tips page -->
<section class="page page--tips">
  <div class="tips__upper">
    <h2 class="tips__heading">Step 2: Elimination</h2>
    <p class="tips__text">Now that you have identified ten, imagine that you are only permitted to have five values. Which five would you give up? Cross them off. Put them into order, the one that is most important to you first. Write it somewhere and refer to it when you can't make a decision, align yourself with what makes you feel good.</p>
    <ol class="tips__blanks">
      <li>1.<span></span></li><li>2.<span></span></li><li>3.<span></span></li><li>4.<span></span></li><li>5.<span></span></li>
    </ol>
    <h2 class="tips__heading">Step 3: Support yourself</h2>
    <p class="tips__text">Write it somewhere and refer to it when you can't make a decision, align yourself with what makes you feel good.</p>
  </div>

  <div class="tips__panel">
    <h2 class="tips__heading">10 tips to improve your wellbeing</h2>
    <p class="tips__intro">Yes, you will have to get off the couch and you might need to say no to burgers for lunch every day but we promise we won't turn you into lycra wearing vegans with prescriptions to Glowmart!<br><br>Small changes every day can make a huge difference.</p>
    <p class="tip"><span class="tip__name">1. Put on your wake up grin</span> – Smile and think happy thoughts – that first 90 secs has a big impact on your day. If you start the day with bad thoughts, then it compounds – simply turn up the corners of your mouth and release feel-good hormones.</p>
    <p class="tip"><span class="tip__name">2. Drink lemon and warm water first thing</span> – and keep drinking water all day. It will cleanse your liver, you will eat less, you'll feel better and have a clearer head.</p>
    <p class="tip"><span class="tip__name">3. Exercise</span> – it boosts the happy chemicals in your brain. So Be Active – get your heart rate going and stretch those muscles. At the very least take the stairs, walk up those stairs faster, do your house work quicker – get that heart pumping.</p>
    <p class="tip"><span class="tip__name">4. Eat a banana</span> – Did you ever see a depressed chimp? Bananas help to lessen feelings of stress and anxiety due to high levels of tryptophan which converts to serotonin – one of those happy hormones.</p>
    <p class="tip"><span class="tip__name">5. Put on your WOW! Glasses</span> – Go outside and Take Notice – The wind, the warmth, the cold, the trees, the blossom, the amazing sky, the moon. Even better, go with a friend and Connect as well.</p>
    <p class="tip"><span class="tip__name">6. 5 fruit and veg per day</span> – Get the fibre into you... Without it you clog up, if you clog up you get grumpy and sluggish – put them into a smoothie.</p>
    <p class="tip"><span class="tip__name">7. Play music</span> – it cheers you up. Create a playlist for when you need a pick-me-up. Play it in the car, doing your housework or on that brisk walk. (No, not the sad break-up playlist!)</p>
    <p class="tip"><span class="tip__name">8. Remove a poison</span> – Take away something that you know is bad for you – fast food, sugar, gluten – even for a couple of days a week – replace it with something healthy like water, fruit, veg, quinoa, exercise.</p>
    <p class="tip"><span class="tip__name">9. Kill em with kindness</span> – When you're feeling bad, do something nice for someone else and it will make their day and you'll feel even better. In fact, Give every day.</p>
    <p class="tip"><span class="tip__name">10. Keep the cogs turning</span> – Use it or lose it as they say – use your brain. Keep learning – something new every day.</p>
  </div>
  <div class="brand tips__brand"><span class="brand__dot"></span>Kestrel Orchard</div>

  <p class="site-url">www.kestrelorchard.co.nz</p>
  <div class="site-bar"></div>
</section>

</body>
</html>
```